Vietnam Motorcycle Trip TRAVEL GUIDE!! Book Cover!

I need an adventurous book cover for a book called "THROTTLE SAGA: A Drifter's Handbook to Crossing the Spine of Vietnam". I would like people to look at the cover and think adventure and Vietnam. I want it to appeal to backpackers and people who have not travelled to Vietnam. A motorbike riding along a road in Vietnam would be ideal with some landscapes to suggest we are definitely in Vietnam. The rear cover could perhaps be one of Vietnam's tropical beaches or something else that says "this place is a paradise". It could also be something else that is quinessentially Vietnamese.

The book will be A5 Dimensions. And it will also need a printable A5 interior cover too. The interior covers can just be images. No text needed. These interior images can be motorcycle related or Vietnam related. Perhaps some images of Vietnam or some Pho or Banh Mi to give it a bit of flavour. Or a long open road with a motorbike on it.

Please leave space in the external rear, lower right hand corner for a barcode.

I've attached some images to gain inspiration from. And a sample chapter.

Colours I'd like to see on there - greens, camoflague perhaps, yellow, brown, blue.

Target Market(s)

Male backpackers aged 18-35 years old. New Zealand and Australian travellers.

Font styles to use
Serif
Sans Serif

Requirements
Must have
• Exterior and Interior covers.
Barcode space.
Title and subtitle.
Synopsis on rear cover.
Exciting title fonts - perhaps Brushstroke or something equally exciting and rugged
Nice to have
• Colours I'd like to see on there - greens, camoflague perhaps, yellow, brown, blue.

A motorbike riding on the open road of Vietnam.

Rice paddies, beaches, Vietnam War stuff perhaps.

A New Zealand Flag
A Vietnam Flag
Should not have
• Scenery from countries outside Southeast Asia

```html
<!DOCTYPE html>
<html lang="en">
<head>
<meta charset="utf-8">
<title>Throttle Saga – Book Cover</title>
<link href="https://fonts.googleapis.com/css2?family=Bebas+Neue&family=Oswald:wght@200;300;400;600&display=swap" rel="stylesheet">
<style>
  :root {
    --ink: #1f1f1f;
    --ink-soft: #2c2c2c;
    --white: #ffffff;
    --sky-top: #7fa3b1;
    --sky-haze: #f4ecd2;
    --hill: #9a9a7c;
    --field: #b9a255;
    --road: #d9b98a;
    --back-peach: #f6d3c0;
    --back-mint: #dfe6d4;
    --back-water: #b9bfae;
    --spine-tone: #f3e4cf;
  }
  * { margin: 0; padding: 0; box-sizing: border-box; }
  html, body { width: 1200px; height: 846px; overflow: hidden; background: #fff; }
  .cover { position: relative; width: 1200px; height: 846px; overflow: hidden; }

  /* Back cover + spine artwork */
  .back-art {
    position: absolute; left: 0; top: 0; width: 628px; height: 846px;
    background:
      radial-gradient(ellipse 300px 260px at 560px 330px, rgba(255,236,200,.9), rgba(255,236,200,0) 70%),
      linear-gradient(180deg, var(--back-mint) 0%, #f2dccb 30%, var(--back-peach) 48%, #e7d6c0 62%, var(--back-water) 80%, #a9ae9c 100%);
  }
  .back-art::after {
    content: ""; position: absolute; left: 0; top: 500px; width: 130px; height: 280px;
    background: linear-gradient(90deg, rgba(110,115,95,.55), rgba(110,115,95,0));
  }

  /* Front cover artwork */
  .front-art {
    position: absolute; left: 628px; top: 0; width: 572px; height: 846px;
    background:
      radial-gradient(circle 180px at 480px 420px, rgba(255,250,230,.95), rgba(255,250,230,0) 70%),
      linear-gradient(180deg, var(--sky-top) 0%, #a9c0c2 22%, #e9e2cc 42%, var(--sky-haze) 56%, var(--hill) 62%, #aaa268 70%, var(--field) 80%, var(--road) 100%);
  }

  /* Back text */
  .blurb {
    position: absolute; left: 40px; top: 38px; width: 515px;
    font-family: "Oswald", sans-serif; font-weight: 300; font-size: 17px;
    line-height: 21.7px; color: var(--ink);
  }
  .blurb p { margin-bottom: 14px; }
  .blurb p.tight { margin-bottom: 0; }
  .blurb em { font-style: italic; }
  .reveals { list-style: none; margin-bottom: 14px; }
  .reveals li { position: relative; padding-left: 34px; }
  .reveals li::before { content: "-"; position: absolute; left: 20px; }
  .bio-heading {
    font-family: "Oswald", sans-serif; font-weight: 600; font-size: 24px;
    line-height: 26px; color: var(--ink); margin-top: 2px;
  }
  .barcode-space {
    position: absolute; left: 359px; top: 697px; width: 196px; height: 117px;
    background: var(--white);
  }

  /* Spine */
  .spine-title, .spine-author {
    position: absolute; left: 600px; transform-origin: 0 0;
    transform: rotate(90deg) translateY(-50%); white-space: nowrap; color: var(--white);
  }
  .spine-title { top: 36px; font-family: "Bebas Neue", sans-serif; font-size: 44px; letter-spacing: .5px; }
  .spine-author { top: 506px; font-family: "Oswald", sans-serif; font-weight: 200; font-size: 36px; color: var(--ink-soft); }

  /* Front text */
  .front-title {
    position: absolute; left: 628px; width: 572px; top: 18px; text-align: center;
    font-family: "Bebas Neue", sans-serif; color: var(--white);
    text-shadow: 0 2px 6px rgba(0,0,0,.25); line-height: .86;
  }
  .front-title .line-1 { display: block; font-size: 136px; }
  .front-title .line-2 { display: block; font-size: 176px; }
  .subtitle {
    position: absolute; left: 628px; width: 572px; top: 292px; text-align: center;
    font-family: "Bebas Neue", sans-serif; font-size: 42px; line-height: 42px; color: var(--ink);
  }
  .front-author {
    position: absolute; left: 628px; width: 572px; top: 752px; text-align: center;
    font-family: "Oswald", sans-serif; font-weight: 200; font-size: 58px; line-height: 1;
    color: var(--white); letter-spacing: -1px;
  }
</style>
</head>
<body>
<main class="cover">
  <div class="back-art" role="img" aria-label="Pastel sunset over a calm bay with limestone karst islands"></div>
  <div class="front-art" role="img" aria-label="Rider on a motorbike travelling down a sunlit country road through golden rice fields towards misty karst mountains"></div>

  <section class="blurb">
    <p>Travel like a pro in a country where bribing cops is normal!</p>
    <p class="tight">Everyone knows someone who’s ridden the length of Vietnam. What if you could do the same?</p>
    <p>For us Kiwis and Australians, it’s difficult finding decent material about motorcycling in Vietnam. With so much conflicting information online and uncertainty around costs, it’s no wonder people keep putting off this 1600 km road trip.</p>
    <p class="tight"><em>Cal Whitfield</em> has been there and done it. In the flesh. And whether your goal is riding from Saigon to Hanoi, across multiple Southeast Asian countries, or just hooning around for a few days, this guide is your bulletproof vest.</p>
    <p class="tight">It reveals…</p>
    <ul class="reveals">
      <li>How to plan your own motorcycle odyssey before leaving home</li>
      <li>Where and how to buy / rent a bike</li>
      <li>What types of licences and insurance you’ll need</li>
      <li>How to finish your trip alive without getting shaken down by dodgy cops or run over by a pig truck</li>
      <li>Itemized expense reports, showing this journey is possible for as little as $90 NZD per day and even as low as $50.</li>
      <li>A day-by-day outline of our riding itinerary</li>
    </ul>
    <p>None of us are getting any younger. And with all the information you need in one lightweight book, what’s stopping you?</p>
    <h2 class="bio-heading">CALLUM WHITFIELD</h2>
    <p>Callum Whitfield has ridden motorbikes since he was a young chap growing up in the wilds of New Zealand. He has lived in four countries and has an honours degree in Anthropology and History. Callum is also the author of The Harbour Storms: Notes of a Student and is always planning the next motorcycle odyssey.</p>
  </section>
  <div class="barcode-space" aria-label="Barcode space"></div>

  <div class="spine-title">THROTTLE SAGA</div>
  <div class="spine-author">CALLUM WHITFIELD</div>

  <h1 class="front-title"><span class="line-1">THROTTLE</span><span class="line-2">SAGA</span></h1>
  <p class="subtitle">A DRIFTER’S HANDBOOK TO<br>CROSSING THE SPINE OF VIETNAM</p>
  <p class="front-author">CALLUM WHITFIELD</p>
</main>
</body>
</html>
```